Business card design needed

We need a business card design for our new company KiraVelle Event Creations, based in Leeton NSW. We will however be serving the whole Riverina area. We plan any events like, Parties, Weddings ext. We would like to see designs that is vibrant but elegant. Mainly we would like to have our Name displayed on the front and all the other info at the back. We need a design that will catch the eye anywhere.Design FRONT AND BACK
Updates

Industry/Entity Type

Events

Contact Information for Business Card

KiraVelle Event Creations
Tessa Verhulst

0461593802
kiravelle@brightmail.example

Dream Beyond Limits

Requirements
Must have
• Elegant Coulors and Fonts

```html
<!DOCTYPE html>
<html lang="en">
<head>
<meta charset="utf-8">
<title>KiraVelle – Business Card</title>
<link href="https://fonts.googleapis.com/css2?family=Cinzel:wght@400&display=swap" rel="stylesheet">
<style>
  :root {
    --backdrop: #3a3a3c;
    --card: #060a13;
    --silver: #d6d6d8;
    --silver-soft: #b4b4b8;
    --rule: #9a9a9f;
  }
  * { margin: 0; padding: 0; box-sizing: border-box; }
  html, body {
    width: 1200px; height: 901px; overflow: hidden;
    background: var(--backdrop);
  }
  .canvas { position: relative; width: 1200px; height: 901px; }
  .card {
    position: absolute; top: 301px; width: 514px; height: 297px;
    background: var(--card);
    box-shadow: 0 6px 14px rgba(0,0,0,.55);
    font-family: "Cinzel", "Times New Roman", serif;
    color: var(--silver);
    text-align: center;
    -webkit-font-smoothing: antialiased;
  }
  .card--front { left: 73px; }
  .card--back { left: 615px; }

  .brand { position: absolute; left: 0; right: 0; }
  .brand__name { display: block; line-height: 1; color: var(--silver); letter-spacing: 1px; }
  .brand__rule { display: block; height: 1px; background: var(--rule); margin-left: auto; margin-right: auto; }
  .brand__sub { display: block; line-height: 1; color: var(--silver-soft); }

  .card--front .brand { top: 118px; }
  .card--front .brand__name { font-size: 36px; }
  .card--front .brand__rule { width: 265px; margin-top: 16px; margin-bottom: 7px; }
  .card--front .brand__sub { font-size: 10px; letter-spacing: 9px; padding-left: 9px; }

  .card--back .brand { top: 40px; }
  .card--back .brand__name { font-size: 26px; }
  .card--back .brand__rule { width: 205px; margin-top: 12px; margin-bottom: 5px; }
  .card--back .brand__sub { font-size: 8px; letter-spacing: 7px; padding-left: 7px; }

  .contact { position: absolute; left: 0; right: 0; top: 141px; line-height: 1; }
  .contact__name { font-size: 19px; letter-spacing: 1px; color: var(--silver); }
  .contact__line { font-size: 14px; margin-top: 11px; color: var(--silver); }
  .contact__email { font-size: 12px; margin-top: 6px; text-transform: uppercase; color: var(--silver); }

  .tagline {
    position: absolute; left: 0; right: 0; top: 258px; line-height: 1;
    font-size: 12px; letter-spacing: 13px; padding-left: 13px; color: var(--silver-soft);
  }
</style>
</head>
<body>
<main class="canvas">
  <section class="card card--front" aria-label="Card front">
    <div class="brand">
      <span class="brand__name">KiraVelle</span>
      <span class="brand__rule"></span>
      <span class="brand__sub">EVENT DESIGN</span>
    </div>
  </section>

  <section class="card card--back" aria-label="Card back">
    <div class="brand">
      <span class="brand__name">KiraVelle</span>
      <span class="brand__rule"></span>
      <span class="brand__sub">EVENT DESIGN</span>
    </div>
    <div class="contact">
      <p class="contact__name">Tessa Verhulst</p>
      <p class="contact__line">0461 593 802</p>
      <p class="contact__email">kiravelle@brightmail.example</p>
    </div>
    <p class="tagline">DREAM BEYOND LIMITS</p>
  </section>
</main>
</body>
</html>
```